Tavlor Suite Background image creation.

We need someone to develop an image that is 1920x1080 using our company logo and and colors. We will be using this as the login page background on tavlorsuite.net for all our clients.

```html
<!DOCTYPE html>
<html lang="en">
<head>
<meta charset="utf-8">
<title>Harborline Networks – Login Background</title>
<link rel="stylesheet" href="https://fonts.googleapis.com/css2?family=Lato:ital,wght@1,700&family=Roboto:wght@400;500&display=swap">
<style>
  :root {
    --page: #ffffff;
    --navy-deep: #121922;
    --navy-mid: #1c2836;
    --slate: #2e445b;
    --steel: #4a6580;
    --cyan: #4fd0f2;
    --white: #ffffff;
  }
  * { margin: 0; padding: 0; box-sizing: border-box; }
  html, body {
    width: 1200px;
    height: 1000px;
    overflow: hidden;
    background: var(--page);
  }
  .canvas {
    position: relative;
    width: 1200px;
    height: 1000px;
    background: var(--page);
  }
  .banner {
    position: absolute;
    left: 0;
    top: 160px;
    width: 1200px;
    height: 680px;
    overflow: hidden;
    background: linear-gradient(90deg, var(--navy-deep) 0%, var(--navy-mid) 45%, var(--slate) 80%, var(--steel) 100%);
  }
  .office-scene {
    position: absolute;
    left: 560px;
    top: 0;
    width: 640px;
    height: 680px;
    background:
      radial-gradient(ellipse 300px 340px at 320px 330px, rgba(110, 170, 210, 0.35), rgba(110, 170, 210, 0) 70%),
      linear-gradient(90deg, rgba(28, 40, 54, 0) 0%, rgba(60, 88, 115, 0.55) 60%, rgba(80, 108, 135, 0.6) 100%);
  }
  .brand {
    position: absolute;
    left: 105px;
    top: 116px;
    display: flex;
    align-items: center;
    gap: 14px;
  }
  .brand-mark {
    width: 22px;
    height: 22px;
    border-radius: 50%;
    background: var(--white);
  }
  .brand-name {
    font-family: "Roboto", sans-serif;
    font-weight: 500;
    font-size: 26px;
    color: var(--white);
    letter-spacing: 0.2px;
  }
  .headline {
    position: absolute;
    left: 101px;
    top: 250px;
    font-family: "Lato", sans-serif;
    font-style: italic;
    font-weight: 700;
    font-size: 66px;
    line-height: 74px;
    color: var(--cyan);
    letter-spacing: -0.5px;
  }
  .tagline {
    position: absolute;
    left: 103px;
    top: 426px;
    font-family: "Roboto", sans-serif;
    font-weight: 400;
    font-size: 27px;
    line-height: 35px;
    color: var(--white);
  }
</style>
</head>
<body>
  <main class="canvas">
    <section class="banner">
      <div class="office-scene" role="img" aria-label="Softly lit modern office interior with a glossy wall-mounted security sign"></div>

      <div class="brand">
        <span class="brand-mark"></span>
        <span class="brand-name">Harborline Networks</span>
      </div>

      <h1 class="headline">Client-Focused.<br>Results-Driven.</h1>

      <p class="tagline">It’s what we do that<br>makes IT work<br>for you</p>
    </section>
  </main>
</body>
</html>
```